Plakate für Haushaltshilfen und Alltagsbegleiter
Zielgruppe
Wir bieten haushaltsnahe Dienstleistungen (Haushaltshilfen und Altgasbegleiter) für Personen mit einem Pflegegrad 1 - 5 an.
Zielgruppe sind Personen mit einem Pflegegrad 1 - 5. Hauptsächlich ältere Menschen die Unterstützung/Betreuung im Alltag und Haushalt benötigen.
Aufgabenstellung
Wir benötigen für unsere Büroräume eine Fensterbeschriftung. Es handelt sich hier um 5 Fenster (Glasflächen) und eine Glastür. Die Vorgabe ist, dass von außen zu erkennen ist dass sich um alle Räumlichkeiten um unsere (Firma Lindwerk) Räumlichkeiten handelt. Desweiteren soll auch unser Angebot erkennbar sein.
Unser Angebot enthält: Haushaltshilfen und Alltagsbegleiter
- kostenlose Haushaltshilfe ab Pflegegrad 1
- Abrechnung mit allen Kostenträgern
Da wir keine Schilder an die Fassade anbringen können, müßen die Glasflächen dafür genutzt werden um zum Einen uns als Firma erkennbar zu machen und zum anderen unser Angebot kurz zu präsentieren.
Uns ist wichtig dass unser Logo verwendet wir und auch unsere Farben.
Desweiteren sollten an den Fenstern auch teilweise eine Sichtschutz nach innen, angebracht werden, aber eben nur teilweise also nicht das ganzen Fenster z.Bsp. mit einer Blickdichten Folie überziehen, sondern in Augenhöhe wenn Fußgänger vorbei laufen.

```html
<!DOCTYPE html>
<html lang="de">
<head>
<meta charset="utf-8">
<title>Lindwerk – Fensterplakate</title>
<link rel="stylesheet" href="https://fonts.googleapis.com/css2?family=Montserrat:wght@800&family=Raleway:wght@400;600;700&display=swap">
<style>
  :root {
    --stage: #5e5e5e;
    --paper: #e4e4e4;
    --paper-light: #f1f1f1;
    --red: #c4232a;
    --red-bright: #e0262c;
    --red-deep: #8e1a1f;
    --ink: #2e2e2e;
    --door-grey: #5a5a5a;
    --white: #ffffff;
  }
  * { box-sizing: border-box; margin: 0; padding: 0; }
  html, body { width: 1200px; height: 733px; overflow: hidden; }
  body { background: var(--stage); position: relative; font-family: "Raleway", sans-serif; }

  .poster {
    position: absolute;
    overflow: hidden;
    background: radial-gradient(circle at 50% 30%, var(--paper-light), var(--paper));
  }
  .poster--benefits { left: 40px;  top: 258px; width: 181px; height: 245px; }
  .poster--support  { left: 229px; top: 258px; width: 181px; height: 245px; }
  .poster--services { left: 421px; top: 258px; width: 181px; height: 245px; }
  .poster--billing  { left: 613px; top: 236px; width: 181px; height: 290px; }
  .poster--door     { left: 815px; top: 206px; width: 143px; height: 318px; background: var(--door-grey); }
  .poster--contact  { left: 980px; top: 236px; width: 181px; height: 290px; }

  .brand { position: absolute; left: 0; right: 0; display: flex; align-items: center; justify-content: center; gap: 6px; }
  .brand__dot { width: 28px; height: 28px; border-radius: 50%; border: 3px solid var(--red); flex: none; }
  .brand__text { display: flex; flex-direction: column; }
  .brand__name { font-family: "Raleway", sans-serif; font-weight: 700; font-size: 17px; letter-spacing: 1px; color: var(--ink); line-height: 1; }
  .brand__tag { font-size: 6.4px; font-weight: 600; color: var(--red); letter-spacing: .3px; margin-top: 2px; }
  .brand--light .brand__dot { border-color: var(--white); }
  .brand--light .brand__name, .brand--light .brand__tag { color: var(--white); }

  .band { position: absolute; left: 0; right: 0; background: var(--ink); color: var(--white);
    font-family: "Montserrat", sans-serif; font-weight: 800; text-align: center; text-transform: uppercase; }
  .band--single { top: 74px; height: 17px; font-size: 10px; line-height: 17px; }
  .band--double { top: 66px; height: 33px; font-size: 9.5px; line-height: 13px; padding-top: 4px; }

  .benefits { position: absolute; top: 98px; left: 10px; right: 10px; display: grid; grid-template-columns: 1fr 1fr; row-gap: 10px; }
  .benefit { text-align: center; font-size: 5.6px; line-height: 1.2; color: var(--ink); }
  .benefit__icon { width: 28px; height: 28px; border-radius: 3px; background: var(--red); margin: 0 auto 3px; }

  .icon-grid { position: absolute; top: 110px; left: 30px; right: 30px; display: grid; grid-template-columns: repeat(3, 1fr); row-gap: 15px; justify-items: center; }
  .icon-grid span { width: 20px; height: 20px; border-radius: 3px; background: var(--red); }

  .wedge { position: absolute; left: 0; width: 100%; display: block; }

  .photo { position: absolute; }
  .photo--hands-cane { left: 0; right: 0; top: 56px; height: 125px;
    background: linear-gradient(135deg, #f2f2f2 0%, #c9c9c9 55%, #8f8f8f 100%); }
  .photo--couple { left: 0; right: 40px; top: 100px; height: 170px;
    background: linear-gradient(180deg, #d0d0d0 0%, #9b9b9b 60%, #6e6e6e 100%); border-radius: 0 40px 0 0; }
  .photo--hands { left: 0; right: 0; top: 56px; height: 75px;
    background: radial-gradient(ellipse at 50% 50%, #bdbdbd 0%, #e6e6e6 60%, var(--paper-light) 100%); }

  .statement { position: absolute; left: 0; right: 0; bottom: 0; height: 64px; background: var(--ink); color: var(--white);
    font-family: "Montserrat", sans-serif; font-weight: 800; font-size: 8.4px; line-height: 11.5px; text-align: center;
    text-transform: uppercase; padding-top: 15px; }

  .price-tag { position: absolute; left: 77px; top: 68px; width: 88px; height: 30px; background: var(--red);
    border-radius: 4px; transform: rotate(-8deg); color: var(--white); font-family: "Montserrat", sans-serif;
    font-weight: 800; font-size: 6.2px; line-height: 7.4px; text-align: center; padding-top: 5px; text-transform: uppercase; }

  .door-copy { position: absolute; left: 12px; right: 10px; top: 121px; color: var(--white);
    font-family: "Montserrat", sans-serif; font-weight: 800; font-size: 7.2px; line-height: 9.8px; text-transform: uppercase; }

  .call-copy { position: absolute; top: 160px; left: 0; right: 0; text-align: center; font-size: 9px; line-height: 11.5px; color: var(--ink); }
  .phone { position: absolute; top: 187px; left: 15px; right: 15px; height: 21px; background: var(--red); border-radius: 5px;
    color: var(--white); font-family: "Montserrat", sans-serif; font-weight: 800; font-size: 13px; line-height: 21px; text-align: center; letter-spacing: .5px; }
  .web { position: absolute; top: 213px; left: 0; right: 0; text-align: center; color: var(--red);
    font-family: "Montserrat", sans-serif; font-weight: 800; font-size: 13px; }
</style>
</head>
<body>

<section class="poster poster--benefits">
  <div class="brand" style="top:18px"><span class="brand__dot"></span><div class="brand__text"><span class="brand__name">LINDWERK</span><span class="brand__tag">HAUSHALTSHILFEN &amp; MEHR</span></div></div>
  <h2 class="band band--single">Unsere Vorteile</h2>
  <div class="benefits">
    <div class="benefit"><div class="benefit__icon"></div>Abrechnung mit allen<br>Pflegekassen möglich</div>
    <div class="benefit"><div class="benefit__icon"></div>Abrechnung über den<br>Entlastungsbetrag von<br>mind. 125 € mtl. ab<br>Pflegegrad 1 möglich</div>
    <div class="benefit"><div class="benefit__icon"></div>Auch über die<br>Verhinderungspflege</div>
    <div class="benefit"><div class="benefit__icon"></div>Hilfe bei der<br>Antragsstellung</div>
  </div>
  <svg class="wedge" style="bottom:0;height:50px" viewBox="0 0 181 50" preserveAspectRatio="none">
    <polygon points="0,16 90,40 181,0 181,50 0,50" fill="var(--red)"/>
    <polygon points="0,28 70,50 0,50" fill="var(--red-deep)"/>
    <polygon points="80,50 181,22 181,50" fill="var(--ink)"/>
  </svg>
</section>

<section class="poster poster--support">
  <div class="brand" style="top:18px"><span class="brand__dot"></span><div class="brand__text"><span class="brand__name">LINDWERK</span><span class="brand__tag">HAUSHALTSHILFEN &amp; MEHR</span></div></div>
  <div class="photo photo--hands-cane" role="img" aria-label="Schwarzweißfoto: eine Hand ruht auf den Händen einer älteren Person am Gehstock"></div>
  <svg class="wedge" style="top:150px;height:45px" viewBox="0 0 181 45" preserveAspectRatio="none">
    <polygon points="0,20 70,8 130,25 181,0 181,45 0,45" fill="var(--red)"/>
    <polygon points="0,30 181,30 181,45 0,45" fill="var(--red-deep)"/>
  </svg>
  <p class="statement">Wir bieten Haushaltshilfen<br>und Altagsbegleiter ab<br>Pflegegrad 1 an</p>
</section>

<section class="poster poster--services">
  <div class="brand" style="top:18px"><span class="brand__dot"></span><div class="brand__text"><span class="brand__name">LINDWERK</span><span class="brand__tag">HAUSHALTSHILFEN &amp; MEHR</span></div></div>
  <h2 class="band band--double">Haushaltshilfe<br>ab Pflegegrad 1</h2>
  <div class="icon-grid" role="img" aria-label="Symbole für Fensterputzen, Wäsche, Reinigen, Staubwischen, Putzmittel, Saugen, Eimer, Wischen, Händewaschen">
    <span></span><span></span><span></span><span></span><span></span><span></span><span></span><span></span><span></span>
  </div>
  <svg class="wedge" style="bottom:0;height:50px" viewBox="0 0 181 50" preserveAspectRatio="none">
    <polygon points="0,16 90,40 181,0 181,50 0,50" fill="var(--red)"/>
    <polygon points="0,28 70,50 0,50" fill="var(--red-deep)"/>
    <polygon points="80,50 181,22 181,50" fill="var(--ink)"/>
  </svg>
</section>

<section class="poster poster--billing">
  <div class="brand" style="top:18px"><span class="brand__dot"></span><div class="brand__text"><span class="brand__name">LINDWERK</span><span class="brand__tag">HAUSHALTSHILFEN &amp; MEHR</span></div></div>
  <p class="price-tag">Abrechnung<br>mit allen<br>Pflegekassen</p>
  <div class="photo photo--couple" role="img" aria-label="Schwarzweißfoto: älteres Paar von hinten, Arm in Arm, mit Gehstock"></div>
  <svg class="wedge" style="bottom:0;height:60px" viewBox="0 0 181 60" preserveAspectRatio="none">
    <polygon points="0,20 90,50 181,0 181,60 0,60" fill="var(--red)"/>
    <polygon points="0,34 70,60 0,60" fill="var(--red-deep)"/>
    <polygon points="80,60 181,26 181,60" fill="var(--ink)"/>
  </svg>
</section>

<section class="poster poster--door">
  <svg class="wedge" style="top:0;height:72px" viewBox="0 0 143 72" preserveAspectRatio="none">
    <polygon points="0,0 143,0 143,18 0,72" fill="var(--red)"/>
    <polygon points="90,0 143,0 143,40 112,16" fill="var(--paper-light)"/>
    <polygon points="0,0 45,0 0,40" fill="var(--red-deep)"/>
  </svg>
  <div class="brand brand--light" style="top:70px"><span class="brand__dot"></span><div class="brand__text"><span class="brand__name" style="font-size:14px">LINDWERK</span><span class="brand__tag" style="font-size:5.4px">HAUSHALTSHILFEN &amp; MEHR</span></div></div>
  <p class="door-copy">Nutzen Sie Ihren Entlastungsbetrag ab Pflegegrad 1 und Ihre Verhinderungspflege ab dem Pflegegrad 2, bevor Ihr Anspruch verfällt</p>
  <svg class="wedge" style="bottom:0;height:54px" viewBox="0 0 143 54" preserveAspectRatio="none">
    <polygon points="0,0 60,6 100,28 143,0 143,54 0,54" fill="var(--red)"/>
    <polygon points="0,26 80,38 143,24 143,54 0,54" fill="var(--white)"/>
  </svg>
</section>

<section class="poster poster--contact">
  <div class="brand" style="top:18px"><span class="brand__dot"></span><div class="brand__text"><span class="brand__name">LINDWERK</span><span class="brand__tag">HAUSHALTSHILFEN &amp; MEHR</span></div></div>
  <div class="photo photo--hands" role="img" aria-label="Schwarzweißfoto: zwei Hände halten sich"></div>
  <p class="call-copy">Buchen Sie gleich hier einen<br>Termin oder rufen Sie uns unter</p>
  <p class="phone">0711 20 48 36 19</p>
  <p class="web">www.lindwerk.de</p>
  <svg class="wedge" style="bottom:0;height:46px" viewBox="0 0 181 46" preserveAspectRatio="none">
    <polygon points="0,16 90,40 181,0 181,46 0,46" fill="var(--red)"/>
    <polygon points="0,26 70,46 0,46" fill="var(--red-deep)"/>
    <polygon points="80,46 181,20 181,46" fill="var(--ink)"/>
  </svg>
</section>

</body>
</html>
```